Casa and Valor Website Re-design

Already Wordpress base. Needs to be updated and better presentation. Current site: www.valorcasa.example redirected from www.casaandvalors.example
Site purpose is to offer information and get leads from potential heroes looking to buy, rent or sell a home
Here is a link to the video to be used as well: https://www.videohost.example/watch?v=Lm8RtPz3VwK

I own the video and logo
The video spells out the program. We will need a page for REALTORS to sign up, a page for our Vendors and their benefits
Steadfast Lending, Marpen Odari offers a reduced rate plus they will pay the upfront cost of the $600 VA appraisal
Hero Buyers get 25% rebate after escrow
Hero Sellers get 25% off a normal 6% Listing
Copperfield Inspections will give a 10% off discount for heroes
Also need a page for the Medic Gives program

Direct competitor: www.nestsforvalor.example

Target Market(s)

veterans, teachers, government employees, nurses, 1st responders

Industry/Entity Type

Realtor

Coding

Coded - Design and coding required

Number of Pages Required

5+ page

Colors
ec1f27
ffffff
3176b5

Requirements
Must have
• clean and correct throughout, ability to collect leads with FB login, or names and phone and email information. Colors are Navy Blue, Burgandy Red, and White
Nice to have
• photos

```html
<!DOCTYPE html>
<html lang="en">
<head>
<meta charset="utf-8">
<title>Casa and Valor</title>
<link href="https://fonts.googleapis.com/css2?family=Roboto:wght@400;500;700&family=Roboto+Condensed:wght@400;700&family=Raleway:wght@400;500&family=Roboto+Slab:wght@300;400&display=swap" rel="stylesheet">
<style>
:root{
  --red:#ec1f27;
  --red-dark:#d8323c;
  --blue:#3176b5;
  --sky:#9fc4f0;
  --navy:#0f2d5c;
  --navy-mid:#1c3f7a;
  --navy-soft:#3f5f90;
  --footer:#06304f;
  --footer-bar:#0a3d63;
  --ink:#222;
  --muted:#666;
  --panel:#f3f3f3;
  --grey:#e4e4e4;
  --white:#fff;
}
*{box-sizing:border-box;margin:0;padding:0}
html,body{width:1200px;height:2550px;overflow:hidden}
body{position:relative;font-family:"Roboto",sans-serif;color:var(--ink);background:var(--white)}
.abs{position:absolute}

/* header */
.topbar{left:0;top:0;width:1200px;height:58px;background:var(--sky)}
.brand{left:162px;top:18px;font:700 34px/1 "Roboto Condensed",sans-serif;color:var(--navy)}
.consult{left:805px;top:12px;color:var(--white);font-size:11px}
.consult strong{display:block;font-size:18px;font-weight:500;margin-top:2px}
.consult svg{position:absolute;left:-40px;top:4px}
.social{top:20px;width:22px;height:22px;border-radius:50%;border:1.5px solid var(--red);background:var(--white)}
.nav{left:0;top:58px;width:1200px;height:48px;background:var(--red);clip-path:polygon(300px 0,1200px 0,1200px 48px,270px 48px,300px 0)}
.nav-bg{left:0;top:58px;width:300px;height:48px;background:var(--sky);clip-path:polygon(0 0,300px 0,270px 48px,0 48px)}
.nav ul{position:absolute;left:358px;top:0;list-style:none;display:flex;gap:42px;height:48px;align-items:center}
.nav li{color:var(--white);font-size:14.5px}

/* hero */
.hero{left:0;top:106px;width:1200px;height:464px;background:linear-gradient(180deg,#6b7a86 0%,#8b8f8c 45%,#5a5040 100%)}
.hero-title{left:0;top:245px;width:1200px;text-align:center;font:700 40px/1 "Roboto Condensed",sans-serif;color:var(--white);letter-spacing:-.5px}
.hero-sub{left:0;top:300px;width:1200px;text-align:center;color:var(--white);font-size:26px}
.hero-sub .pct{display:inline-block;background:var(--red);border-radius:4px;padding:6px 12px;margin-right:8px;font-weight:500}
.hero-sub .pct b{font-size:32px}

.tiles{left:162px;top:500px;width:877px;height:136px;display:flex}
.tile{flex:1;background:var(--navy);border-right:1px solid #4a6796;color:var(--white);text-align:center;font:700 17px "Roboto Condensed",sans-serif;padding-top:22px}
.tile:last-child{background:var(--navy-soft);border:none}
.tile .ico{width:76px;height:76px;margin:0 auto 10px;border:2px solid var(--white);border-radius:10px;display:flex;align-items:center;justify-content:center}

/* welcome */
.video-shadow{left:190px;top:712px;width:383px;height:252px;background:var(--grey)}
.video{left:162px;top:687px;width:386px;height:253px;background:linear-gradient(135deg,#2c5aa8,#1a3c80);border:3px solid #4a86cf}
.welcome-kicker{left:597px;top:683px;font:400 26px "Raleway",sans-serif;color:var(--red);letter-spacing:1px}
.welcome-title{left:597px;top:715px;font:500 19px "Raleway",sans-serif;letter-spacing:3px}
.welcome-text{left:597px;top:752px;width:440px;font-size:11.5px;line-height:1.65;color:var(--muted)}
.serving{left:597px;top:866px;width:380px;padding-bottom:8px;border-bottom:2px solid var(--navy-mid);font:400 22px "Roboto",sans-serif}
.contact-chip{top:920px;display:flex;gap:10px}
.contact-chip .sq{width:48px;height:44px;border:2px solid var(--navy-mid);display:flex;align-items:center;justify-content:center}
.contact-chip small{display:block;color:var(--blue);font-size:14px}
.contact-chip span{font:700 21px "Roboto Condensed",sans-serif}
.contact-chip span.plain{font:400 13px "Roboto",sans-serif}

/* stats */
.rule{left:0;top:1035px;width:1200px;height:3px;background:var(--blue)}
.stats{left:0;top:1038px;width:1200px;height:196px;display:flex}
.stat{flex:1;background:var(--grey);display:flex;align-items:center;justify-content:center}
.stat:nth-child(even){background:var(--panel)}
.circle{width:152px;height:152px;border-radius:50%;border:2px solid #e6c3c8;background:rgba(255,255,255,.35);display:flex;flex-direction:column;align-items:center;justify-content:center;text-align:center;font:400 19px/1.1 "Roboto Condensed",sans-serif}
.circle b{color:var(--red);font:700 26px "Roboto Condensed",sans-serif}
.circle b small{font-size:15px;color:var(--ink);font-weight:400}
.band{left:0;top:1234px;width:1200px;height:38px;background:var(--red-dark);color:var(--white);text-align:center;font-size:15px;line-height:38px}

/* blog */
.blog-head{left:162px;top:1316px;font:300 31px "Roboto Slab",serif}
.blog-line{left:412px;top:1336px;width:403px;height:3px;background:#4aa3e0}
.arrow-btn{top:1326px;width:22px;height:22px;border:1px solid #ccc;color:#999;font-size:12px;text-align:center;line-height:20px}
.card{top:1382px;width:287px;height:287px;background:var(--blue);color:var(--white)}
.card .ph{height:136px}
.card h3{margin:24px 14px 8px;font-size:14.5px;font-weight:500}
.card .meta{margin:0 14px 12px;font-size:10px}
.card p{margin:0 14px;font-size:10.5px;line-height:1.6}
.side{left:762px;width:277px;display:flex;gap:8px}
.side .th{width:99px;height:70px;flex:none}
.side h4{font:400 12px/1.25 "Roboto Slab",serif;color:var(--blue)}
.side p{font-size:9.5px;color:var(--muted);line-height:1.4;margin-top:3px}
.side a{font-size:9.5px;color:var(--blue)}

/* map + contact */
.map{left:0;top:1705px;width:1200px;height:326px;background:linear-gradient(160deg,#e8e8e8,#d9d9d9)}
.info{left:162px;top:1923px;width:877px;height:253px;display:flex;gap:2px}
.info .col{flex:1;background:var(--panel);text-align:center;padding-top:52px}
.info h5{font-size:16px;font-weight:400;margin:14px 0 10px}
.info .big{color:var(--blue);font-size:18px;font-weight:500}
.info .addr-name{color:var(--blue);font-size:15px;font-weight:700}
.info .small{font-size:12px;color:#555}
.info .link{color:var(--blue);font-size:15px;margin-top:40px}
.info .link.tight{margin-top:22px}

/* footer */
.footer{left:0;top:2230px;width:1200px;height:279px;background:var(--footer)}
.foot-brand{left:162px;top:2340px;font:700 40px "Roboto Condensed",sans-serif;color:var(--white)}
.foot-h{color:var(--white);font-size:17px;padding-bottom:12px;border-bottom:1px solid #3c6184}
.foot-about{left:415px;top:2266px;width:287px}
.foot-about p{color:#dfe6ee;font-size:10.5px;line-height:1.6;margin-top:14px}
.connect{left:415px;top:2440px;width:287px;border-top:1px solid #3c6184;padding-top:10px;color:var(--white);font-size:15px;display:flex;align-items:center;gap:10px}
.connect i{width:22px;height:22px;border-radius:50%;background:#d8dde3}
.foot-form{left:761px;top:2266px;width:276px}
.field{height:26px;margin-top:6px;background:#0c3a5d;border:1px solid #2a5578;color:#8aa3ba;font-size:10px;line-height:24px;padding-left:8px}
.field:first-of-type{margin-top:18px}
.submit{display:inline-block;margin-top:18px;background:var(--red-dark);border:1px solid #f06a70;color:var(--white);font-size:12px;font-weight:700;padding:9px 20px}
.copy{left:0;top:2509px;width:1200px;height:41px;background:var(--footer-bar);color:#dfe6ee;text-align:center;font-size:12px;line-height:41px}
</style>
</head>
<body>

<header>
  <div class="abs topbar"></div>
  <div class="abs brand">Casa and Valor</div>
  <div class="abs consult">
    <svg width="28" height="22" viewBox="0 0 28 22"><path d="M3 8c0-5 22-5 22 0l-3 2-4-2v-2H10v2l-4 2z M7 12h14l3 8H4z" fill="#fff"/></svg>
    Schedule a Consultation:<strong>(555) 014 2287</strong>
  </div>
  <div class="abs social" style="left:948px"></div>
  <div class="abs social" style="left:982px"></div>
  <div class="abs social" style="left:1016px"></div>
  <div class="abs nav-bg"></div>
  <nav class="abs nav">
    <ul><li>Home</li><li>How IT Works</li><li>Hero Advantages</li><li>Realtors</li><li>Medic Gives program</li><li>Contact</li></ul>
  </nav>
</header>

<section>
  <div class="abs hero" role="img" aria-label="Photo of a large two-storey white house with a wraparound porch beside a bare tree"></div>
  <h1 class="abs hero-title">COPPERFIELD INSPECTIONS WILL GIVE</h1>
  <p class="abs hero-sub"><span class="pct"><b>10%</b> off</span>discount for heroes</p>
  <div class="abs tiles">
    <div class="tile"><div class="ico"><svg width="48" height="44" viewBox="0 0 48 44" fill="none" stroke="#fff" stroke-width="3"><path d="M4 22 24 4l20 18M10 18v22h28V18"/><path d="M24 18v16M29 21h-7a3 3 0 0 0 0 6h4a3 3 0 0 1 0 6h-7"/></svg></div>YOU BUY A HOME</div>
    <div class="tile"><div class="ico"><svg width="48" height="44" viewBox="0 0 48 44" fill="none" stroke="#fff" stroke-width="3"><path d="M4 22 24 4l20 18M10 18v22h28V18"/><circle cx="22" cy="28" r="6"/><path d="M26 32l8 6"/></svg></div>YOU SELL A HOME</div>
    <div class="tile"><div class="ico"><svg width="48" height="44" viewBox="0 0 48 44" fill="none" stroke="#fff" stroke-width="3"><path d="M8 20 24 6l16 14M12 17v10M36 17v10"/><path d="M4 32c8 0 10 6 20 6s12-6 20-6"/><path d="M24 14v14M28 16h-5a2.5 2.5 0 0 0 0 5h3a2.5 2.5 0 0 1 0 5h-5"/></svg></div>REFINANCE A HOME</div>
  </div>
</section>

<section>
  <div class="abs video-shadow"></div>
  <div class="abs video" role="img" aria-label="Video thumbnail illustration introducing the local hero program"></div>
  <p class="abs welcome-kicker">WELCOME TO</p>
  <h2 class="abs welcome-title">Casa and Valor!</h2>
  <p class="abs welcome-text">Lorem Ipsum is simply dummy text of the printing and typesetting industry. Lorem Ipsum has been the industry's standard dummy text ever since the 1500s, when an unknown printer took a galley of type and scrambled it to make a type specimen book. It has survived not only five centuries, but also the leap into electronic typesetting, remaining essentially unchanged.</p>
  <h3 class="abs serving">Serving Casa and Valor</h3>
  <div class="abs contact-chip" style="left:599px">
    <div class="sq"><svg width="20" height="20" viewBox="0 0 24 24"><path d="M6 2l4 5-2 3c1 3 3 5 6 6l3-2 5 4-3 4C10 22 2 14 2 5z" fill="#d8323c"/></svg></div>
    <div><small>Phone:</small><span>(555) 014 2287</span></div>
  </div>
  <div class="abs contact-chip" style="left:805px">
    <div class="sq"><svg width="22" height="16" viewBox="0 0 22 16"><rect width="22" height="16" fill="#d8323c"/><path d="M0 0l11 9 11-9" fill="none" stroke="#fff" stroke-width="1.6"/></svg></div>
    <div><small>email:</small><span class="plain">info@valorcasa.example</span></div>
  </div>
</section>

<section>
  <div class="abs rule"></div>
  <div class="abs stats">
    <div class="stat"><div class="circle"><b>$600</b>Steadfast Lending</div></div>
    <div class="stat"><div class="circle"><b>25%</b>Hero Buyers get</div></div>
    <div class="stat"><div class="circle"><b>25% <small>Off</small></b>Hero Sellers</div></div>
    <div class="stat"><div class="circle"><b>10% <small>Off</small></b>Copperfield<br>Inspections</div></div>
  </div>
  <p class="abs band">Our community police officers strive to work with residents to make our community one of the safest in the country.</p>
</section>

<section>
  <h2 class="abs blog-head">Latest Blog &amp; News:</h2>
  <div class="abs blog-line"></div>
  <div class="abs arrow-btn" style="left:990px">&#8249;</div>
  <div class="abs arrow-btn" style="left:1017px">&#8250;</div>

  <article class="abs card" style="left:162px">
    <div class="ph" role="img" aria-label="Photo of a family relaxing together on a sofa" style="background:linear-gradient(135deg,#b07a3a,#5a3a22)"></div>
    <h3>Lorem Ipsum is simply dummy text...</h3>
    <p class="meta">June 3, 2017 &nbsp;|&nbsp; Comments &nbsp;|&nbsp; User</p>
    <p>Lorem Ipsum is simply dummy text of the printing and typesetting industry. Lorem Ipsum has been the industry's standard dummy text ever since the 1500s.</p>
  </article>
  <article class="abs card" style="left:461px">
    <div class="ph" role="img" aria-label="Photo of two police officers standing together" style="background:linear-gradient(135deg,#d8d8d8,#3a3a44)"></div>
    <h3>Lorem Ipsum is simply dummy text...</h3>
    <p class="meta">June 3, 2017 &nbsp;|&nbsp; Comments &nbsp;|&nbsp; User</p>
    <p>Lorem Ipsum is simply dummy text of the printing and typesetting industry. Lorem Ipsum has been the industry's standard dummy text ever since the 1500s.</p>
  </article>

  <div class="abs side" style="top:1382px">
    <div class="th" role="img" aria-label="Photo of firefighters at work" style="background:linear-gradient(135deg,#3a5a8a,#b0503a)"></div>
    <div><h4>Lorem Ipsum is simply dummy text of the printing</h4><p>Lorem Ipsum is simply dummy text of the printing and typesetting industry.</p><a>Read More...</a></div>
  </div>
  <div class="abs side" style="top:1472px">
    <div class="th" role="img" aria-label="Photo of a fire engine crew" style="background:linear-gradient(135deg,#8a1f22,#3a3a44)"></div>
    <div><h4>Lorem Ipsum is simply dummy text of the printing</h4><p>Lorem Ipsum is simply dummy text of the printing and typesetting industry.</p><a>Read More...</a></div>
  </div>
  <div class="abs side" style="top:1557px">
    <div class="th" role="img" aria-label="Photo of nurses in blue scrubs" style="background:linear-gradient(135deg,#7fb0d8,#3a6a9a)"></div>
    <div><h4>Lorem Ipsum is simply dummy text of the printing</h4><p>Lorem Ipsum is simply dummy text of the printing and typesetting industry.</p><a>Read More...</a></div>
  </div>
</section>

<section>
  <div class="abs map" role="img" aria-label="Street map showing the office location"></div>
  <div class="abs info">
    <div class="col">
      <svg width="22" height="32" viewBox="0 0 22 32"><path d="M11 0a11 11 0 0 1 11 11c0 8-11 21-11 21S0 19 0 11A11 11 0 0 1 11 0z" fill="#3176b5"/><circle cx="11" cy="11" r="4" fill="#f3f3f3"/></svg>
      <h5>Our Address:</h5>
      <p class="addr-name">Casa and Valor</p>
      <p class="small">1060 Ember Ridge Pkwy Fairhaven,<br>NV 89000</p>
      <p class="link tight">&#10230; Directions</p>
    </div>
    <div class="col">
      <svg width="30" height="30" viewBox="0 0 24 24"><path d="M6 2l4 5-2 3c1 3 3 5 6 6l3-2 5 4-3 4C10 22 2 14 2 5z" fill="#3176b5"/></svg>
      <h5>Phone:</h5>
      <p class="big">(555) 014 2287</p>
      <p class="link">&#10230; Call To Us</p>
    </div>
    <div class="col">
      <svg width="30" height="22" viewBox="0 0 22 16"><rect width="22" height="16" fill="#3176b5"/><path d="M0 0l11 9 11-9" fill="none" stroke="#f3f3f3" stroke-width="1.6"/></svg>
      <h5>Email:</h5>
      <p style="font-size:16px;color:#555">info@valorcasa.example</p>
      <p class="link">&#10230; Send Message</p>
    </div>
  </div>
</section>

<footer>
  <div class="abs footer"></div>
  <div class="abs foot-brand">Casa and Valor</div>
  <div class="abs foot-about">
    <h4 class="foot-h">About us</h4>
    <p>Lorem Ipsum is simply dummy text of the printing and typesetting industry. Lorem Ipsum has been the industry's standard dummy text ever since the 1500s, when an unknown printer took a galley of type and scrambled it to make a type specimen book. It has survived not only...</p>
  </div>
  <div class="abs connect">Connect with us <i></i><i></i><i></i></div>
  <div class="abs foot-form">
    <h4 class="foot-h">Contact Us:</h4>
    <div class="field">NAME</div>
    <div class="field">YOUR EMAIL</div>
    <div class="field">PHONE</div>
    <span class="submit">SUBMIT</span>
  </div>
  <p class="abs copy">Copyright © 2017 — Casa and Valor. All Rights Reserved.</p>
</footer>

</body>
</html>
```